Create a wordpress website for Dulvane business solution

This project is to create a complete website with all pages.

Overview
The purpose of this project is to create a full complete website with all pages (16 pages). The site should be professional and modern. The site is for an IT recruiting and IT training company. The site needs to be easy to administer and update content. It should be simple to add pages, videos and testimonials later. I will leave the site layout, color schemes and flow to the designers.

Navigation Menu (Home, who we are, what we do, what makes us different, why it matters, candidate portal, contact us, Blog)

WHO WE ARE should be a drop down menu with link to pages (about us, mission, vision and purpose, our team)

WHAT WE DO should be drop down menu with link to the following pages (IT Recruiting, IT Training, Hardware and software sales)

What makes us different should be single page with different paragraph titles. (We live what we do, we don't compromise quality, we share knowledge, staffing guarantee)

Why it matters should be single page with paragraph titles. (Quickly fill positions, candidate career development)

Candidate portal should links to my portal login page. I can add the correct URL later. I just need it to link to somewhere. I can change it.

Contact us should have (address, phone number, google map and a form to submit request for a call back)

Blog - This link should launch a wordpress blogging module

Target Market(s)

IT RECRUITING AND CONSULTING

Industry/Entity Type

It Company

Coding

Coded - Design and coding required

Requirements
Must have
• Company Logo
• Navigation Menu (Home, who we are, what we do, what makes us different, why it matters, candidate portal, contact us)
• WHO WE ARE should be a drop down menu with link to pages (about us, mission, vision and purpose, our team)
• WHAT WE DO should be drop down menu with link to the following pages (IT Recruiting, IT Training, Hardware and software sales)
• What makes us different should be single page with different paragraph titles. (We live what we do, we don't compromise quality, we share knowledge, staffing guarantee)
• Why it matters should be single page with paragraph titles. (Quickly fill positions, candidate career development)
• Candidate portal should links to my portal login page. I can add the correct URL later. I just need it to link to somewhere. I can change it.
• Contact us should have (address, phone number, google map and a form to submit request for a call back)

```html
<!DOCTYPE html>
<html lang="en">
<head>
<meta charset="utf-8">
<title>Dulvane Business Solution</title>
<link href="https://fonts.googleapis.com/css2?family=Montserrat:wght@300;400;500;600;700&display=swap" rel="stylesheet">
<style>
:root{
  --blue:#0b5cab;
  --blue-dark:#08498a;
  --orange:#f5a043;
  --ink:#1f2a36;
  --grey:#8a94a0;
  --light-grey:#b9c0c8;
  --line:#e3e7eb;
  --white:#ffffff;
}
*{margin:0;padding:0;box-sizing:border-box}
html,body{width:1200px;height:3403px;overflow:hidden}
body{position:relative;font-family:'Montserrat',Arial,sans-serif;color:var(--ink);background:var(--white)}
.abs{position:absolute}
a{color:inherit;text-decoration:none}

/* header */
.brand{left:86px;top:26px;display:flex;align-items:center;gap:10px}
.brand-mark{width:14px;height:14px;background:var(--orange)}
.brand-name{font-size:26px;font-weight:600;color:var(--blue);letter-spacing:-.3px}
.social{display:flex;gap:24px}
.social span{display:block;width:18px;height:18px;border-radius:50%;background:var(--blue)}
.top-social{left:692px;top:36px}
.top-phone{left:812px;top:33px;display:flex;align-items:center;gap:10px;font-size:19px;font-weight:500;color:var(--ink)}
.login{left:991px;top:27px;width:121px;height:37px;background:var(--blue);color:#fff;font-size:12px;font-weight:600;display:flex;align-items:center;justify-content:center;gap:30px;letter-spacing:.5px}
.nav{left:0;top:91px;width:1200px;height:50px;border-top:1px solid var(--line);border-bottom:1px solid var(--line)}
.nav ul{list-style:none;position:absolute;left:86px;top:0;height:48px;width:985px;display:flex;justify-content:space-between;align-items:center}
.nav li{font-size:11.5px;font-weight:500;letter-spacing:.3px;color:var(--ink)}
.nav li.active{color:var(--blue);font-weight:700}
.nav .search{position:absolute;left:1094px;top:15px}

/* hero */
.hero{left:0;top:141px;width:1200px;height:444px}
.hero-photo{position:absolute;inset:0;background:linear-gradient(90deg,#2c5fa3 0%,#4a77b6 14%,#d77f6b 15%,#e39477 50%,#d0786a 85%,#4a77b6 86%,#2c5fa3 100%)}
.hero-center{left:0;width:1200px;text-align:center;color:#fff}
.hero-kicker{top:106px;font-size:27px;font-weight:300;letter-spacing:1.5px}
.hero-title{top:134px;font-size:68px;font-weight:600;letter-spacing:1px}
.dots{display:flex;gap:5px;justify-content:center}
.dots i{display:block;width:5px;height:5px;background:#fff}
.hero-dots{top:215px}
.hero-text{top:232px;left:270px;width:660px;font-size:15px;line-height:22px;font-weight:500;color:#fff;text-align:center}
.scroll-mouse{left:588px;top:335px}

/* who we are */
.tablet{left:95px;top:662px;width:456px;height:461px;border:2px solid #d9dde2;border-bottom:none;border-radius:34px 34px 0 0;background:#f4f5f7}
.tablet-screen{position:absolute;left:24px;top:58px;width:404px;height:401px;background:linear-gradient(135deg,#2a4f76,#4d7fa8 55%,#2d4a66)}
.tablet-cam{position:absolute;left:222px;top:26px;width:8px;height:8px;border-radius:50%;background:#555}
.section-title{font-size:34px;font-weight:600;color:var(--blue);letter-spacing:.5px;white-space:nowrap}
.orange-dots{position:absolute;display:flex;gap:3px}
.orange-dots i{display:block;width:4px;height:4px;background:var(--orange)}
.who-title{right:86px;top:690px}
.who-lead{left:610px;top:740px;width:504px;text-align:right;font-size:14px;font-weight:600;line-height:20px}
.who-body{left:590px;top:816px;width:524px;text-align:right;font-size:11.5px;line-height:20px;color:#4d5763}
.btn-orange{left:955px;top:1007px;width:157px;height:36px;background:var(--orange);color:#fff;font-size:11px;font-weight:700;display:flex;align-items:center;justify-content:space-between;padding:0 16px 0 22px;letter-spacing:.5px}
.rule{left:0;width:1200px;height:1px;background:var(--line)}

/* what we do */
.do-title{left:86px;top:1210px}
.do-lead{left:86px;top:1259px;width:740px;font-size:13px;font-weight:600;line-height:20px}
.btn-outline{border:1.5px solid var(--blue);color:var(--blue);font-size:11px;font-weight:700;display:flex;align-items:center;justify-content:center;letter-spacing:.5px}
.visit-blog{left:980px;top:1252px;width:132px;height:36px}
.card{width:499px;height:236px;overflow:hidden}
.card-photo{position:absolute;inset:0}
.card-label{position:absolute;right:0;bottom:0;width:311px;height:68px;background:rgba(11,92,171,.92);color:#fff;font-size:25px;font-weight:600;display:flex;align-items:center;justify-content:space-between;padding:0 24px 0 34px}
.card-open{position:absolute;inset:0;background:rgba(11,72,150,.88);color:#fff;padding:50px 32px}
.card-open h3{font-size:25px;font-weight:600;margin-bottom:12px}
.card-open p{font-size:13px;line-height:20px;font-weight:600;width:400px}
.card-open .chev{position:absolute;right:30px;bottom:22px}

/* cta */
.cta{left:0;top:1942px;width:1200px;height:172px;background:var(--blue-dark)}
.cta h2{position:absolute;left:86px;top:52px;color:#fff;font-size:26px;font-weight:600;letter-spacing:.3px}
.cta p{position:absolute;left:86px;top:90px;width:700px;color:#fff;font-size:13px;font-weight:500;line-height:20px}
.cta .contact-btn{position:absolute;left:853px;top:61px;width:261px;height:52px;border:1.5px solid #fff;color:#fff;font-size:12px;font-weight:600;display:flex;align-items:center;justify-content:center;letter-spacing:1px}

/* believe */
.quote-mark{left:340px;top:2150px;font-size:260px;line-height:1;font-weight:700;color:#e6e9ed;font-family:Georgia,serif}
.believe-small{left:86px;top:2238px;font-size:46px;font-weight:300;color:#4a5560;letter-spacing:2px}
.believe-big{left:82px;top:2282px;font-size:86px;font-weight:300;color:var(--blue);letter-spacing:1px}
.believe-text{left:510px;top:2246px;width:570px;font-size:26px;line-height:36px;font-weight:300;color:var(--light-grey)}
.btn-blue{background:var(--blue-dark);color:#fff;font-size:12px;font-weight:700;display:flex;align-items:center;justify-content:center;letter-spacing:.5px;box-shadow:0 4px 0 #063a70}
.testimonials{left:510px;top:2418px;width:261px;height:48px}

/* contact */
.contact-kicker{left:86px;top:2670px;font-size:21px;font-weight:300;color:var(--grey);letter-spacing:.5px}
.contact-title{left:84px;top:2698px;font-size:50px;font-weight:600;color:var(--blue-dark);letter-spacing:.5px;white-space:nowrap}
.contact-band{left:0;top:2799px;width:1200px;height:456px;background:var(--blue-dark)}
.portrait{left:771px;top:2620px;width:429px;height:635px;background:linear-gradient(180deg,#f2f2f2 0%,#e8e4e0 40%,#f6f6f6 100%)}
.call-line{left:86px;top:2826px;color:#fff;font-size:16px;font-weight:400}
.call-line b{font-weight:600}
.field{background:#fff;border:1px solid #d3d8de;color:#9aa3ad;font-size:12px;padding:15px 22px}
.f-name{left:86px;top:2876px;width:347px;height:48px}
.f-email{left:463px;top:2876px;width:347px;height:48px}
.f-msg{left:86px;top:2949px;width:724px;height:167px}
.send{left:86px;top:3141px;width:216px;height:50px;background:#0a4f96;color:#fff;font-size:11px;font-weight:700;display:flex;align-items:center;justify-content:space-between;padding:0 26px 0 32px;letter-spacing:.5px;box-shadow:0 3px 6px rgba(0,0,0,.2)}
.wish{left:426px;top:3143px;color:#fff;font-size:13px;font-weight:600;line-height:20px}
.ico-box{width:52px;height:50px;background:#fff;border:1.5px solid var(--blue);display:flex;align-items:center;justify-content:center}
.ico-phone{left:699px;top:3137px}
.ico-mail{left:758px;top:3137px}

/* footer */
.footer{left:0;top:3255px;width:1200px;height:148px;background:#fff}
.f-brand{left:86px;top:3316px}
.copy{left:274px;top:3324px;font-size:11px;color:var(--grey)}
.f-sep{left:350px;top:3305px;width:1px;height:44px;background:var(--line)}
.f-links{left:385px;top:3324px;display:flex;gap:24px;font-size:11px;font-weight:500;list-style:none}
.f-links .active{color:var(--blue);font-weight:700}
.f-social{left:962px;top:3322px}
.to-top{left:1059px;top:3300px;width:55px;height:57px;border:1px solid var(--line);display:flex;align-items:center;justify-content:center}
</style>
</head>
<body>

<header>
  <a class="abs brand" href="#"><span class="brand-mark"></span><span class="brand-name">Dulvane Business Solution</span></a>
  <div class="abs social top-social"><span aria-label="Social profile 1"></span><span aria-label="Social profile 2"></span></div>
  <div class="abs top-phone">
    <svg width="16" height="16" viewBox="0 0 24 24"><path d="M6.6 10.8c1.4 2.8 3.8 5.1 6.6 6.6l2.2-2.2c.3-.3.7-.4 1-.2 1.1.4 2.3.6 3.6.6.6 0 1 .4 1 1V20c0 .6-.4 1-1 1C10.6 21 3 13.4 3 4c0-.6.4-1 1-1h3.5c.6 0 1 .4 1 1 0 1.3.2 2.5.6 3.6.1.3 0 .7-.2 1z" fill="#1f2a36"/></svg>
    555 014 2290
  </div>
  <a class="abs login" href="#">LOGIN
    <svg width="16" height="16" viewBox="0 0 24 24" fill="none" stroke="#fff" stroke-width="2"><path d="M14 4h6v16h-6M4 12h11M11 8l4 4-4 4"/></svg>
  </a>
  <nav class="abs nav">
    <ul>
      <li class="active">HOME</li><li>WHO WE ARE</li><li>WHAT WE DO</li><li>WHAT MAKES US DIFFERENT</li><li>WHY IT MATTERS</li><li>CANDIDATE PORTAL</li><li>CONTACT US</li><li>BLOG</li>
    </ul>
    <svg class="search" width="18" height="18" viewBox="0 0 24 24" fill="none" stroke="#1f2a36" stroke-width="2.2"><circle cx="10" cy="10" r="7"/><path d="M15 15l6 6"/></svg>
  </nav>
</header>

<section class="abs hero">
  <div class="hero-photo" role="img" aria-label="Photo of smiling professionals seated in a row, tinted blue at the sides and warm orange in the centre"></div>
  <p class="abs hero-center hero-kicker">WELCOME TO</p>
  <h1 class="abs hero-center hero-title">DULVANE LLC</h1>
  <div class="abs hero-center hero-dots dots"><i></i><i></i><i></i></div>
  <p class="abs hero-text">Ut wisi enim ad minim veniam, quis nostrud exerci tation ullamcorper suscipit lobortis nisl ut aliquip ex ea commodo consequat.</p>
  <svg class="abs scroll-mouse" width="24" height="60" viewBox="0 0 24 60" fill="none" stroke="#fff" stroke-width="2"><rect x="3" y="2" width="18" height="30" rx="9"/><path d="M12 9v6M7 46l5 5 5-5"/></svg>
</section>

<section class="who">
  <div class="abs tablet">
    <span class="tablet-cam"></span>
    <div class="tablet-screen" role="img" aria-label="Illustration of a hand touching a network of people icons around a magnifying glass"></div>
  </div>
  <h2 class="abs section-title who-title">WHO WE ARE<span class="orange-dots" style="right:-2px;top:-8px"><i></i><i></i><i></i></span></h2>
  <p class="abs who-lead">Ut wisi enim ad minim veniam, quis nostrud exerci tation ullamcorper suscipit lobortis nisl ut aliquip ex ea commodo consequat.</p>
  <p class="abs who-body">Lorem ipsum dolor sit amet, consectetuer adipiscing elit, sed diam nonummy nibh euismod tincidunt ut laoreet dolore magna aliquam erat volutpat. Ut wisi enim ad minim veniam, quis nostrud exerci tation ullamcorper suscipit lobortis nisl ut aliquip ex ea commodo consequat. Duis autem vel eum iriure dolor in hendrerit in vulputate velit esse molestie consequat, vel illum dolore eu feugiat nulla facilisis at vero eros et accumsan et iusto odio dignissim qui blandit praesent luptatum zzril delenit augue duis dolore te feugait nulla facilisi.</p>
  <a class="abs btn-orange" href="#">LEARN MORE <span style="font-size:18px;font-weight:400">+</span></a>
</section>
<div class="abs rule" style="top:1123px"></div>

<section class="services">
  <h2 class="abs section-title do-title">WHAT WE DO<span class="orange-dots" style="right:-2px;top:-8px"><i></i><i></i><i></i></span></h2>
  <p class="abs do-lead">Ut wisi enim ad minim veniam, quis nostrud exerci tation ullamcorper suscipit lobortis nisl ut aliquip ex ea commodo consequat.</p>
  <a class="abs btn-outline visit-blog" href="#">VISIT BLOG</a>

  <div class="abs card" style="left:86px;top:1334px">
    <div class="card-photo" role="img" aria-label="Photo of people working at laptops" style="background:linear-gradient(135deg,#1c3b63,#3a5f86)"></div>
    <div class="card-open">
      <h3>IT Recruiting</h3>
      <p>Ut wisi enim ad minim veniam, quis nostrud exerci tation ullamcorper suscipit lobortis nisl ut aliquip ex ea commodo consequat.</p>
      <svg class="chev" width="14" height="22" viewBox="0 0 14 22" fill="none" stroke="#fff" stroke-width="3"><path d="M3 3l8 8-8 8"/></svg>
    </div>
  </div>
  <div class="abs card" style="left:615px;top:1334px">
    <div class="card-photo" role="img" aria-label="Photo of a business team meeting around a table" style="background:linear-gradient(135deg,#9a9189,#5d5650 60%,#8a8078)"></div>
    <div class="card-label">IT Training<svg width="14" height="22" viewBox="0 0 14 22" fill="none" stroke="#fff" stroke-width="3"><path d="M3 3l8 8-8 8"/></svg></div>
  </div>
  <div class="abs card" style="left:86px;top:1604px">
    <div class="card-photo" role="img" aria-label="Photo of a green circuit board close-up" style="background:linear-gradient(135deg,#2e5a5c,#123033 60%,#3f6e6c)"></div>
    <div class="card-label">Hardware Sales<svg width="14" height="22" viewBox="0 0 14 22" fill="none" stroke="#fff" stroke-width="3"><path d="M3 3l8 8-8 8"/></svg></div>
  </div>
  <div class="abs card" style="left:615px;top:1604px">
    <div class="card-photo" role="img" aria-label="Photo of hands holding a smartphone with floating app icons" style="background:linear-gradient(135deg,#5a4a3a,#a07a52 55%,#3d3430)"></div>
    <div class="card-label">Software Sales<svg width="14" height="22" viewBox="0 0 14 22" fill="none" stroke="#fff" stroke-width="3"><path d="M3 3l8 8-8 8"/></svg></div>
  </div>
</section>

<section class="abs cta">
  <h2>HAVE MORE QUESTIONS?</h2>
  <p>Ut wisi enim ad minim veniam, quis nostrud exerci tation ullamcorper suscipit lobortis nisl ut aliquip ex ea commodo consequat.</p>
  <a class="contact-btn" href="#">CONTACT US</a>
</section>

<section class="believe">
  <div class="abs quote-mark" aria-hidden="true">&#8220;</div>
  <p class="abs believe-small">WHAT WE</p>
  <h2 class="abs believe-big">BELIEVE</h2>
  <p class="abs believe-text">Lorem ipsum dolor sit amet, consectetuer adipiscing elit, sed diam nonummy nibh euismod tincidunt ut laoreet dolore magna aliquam erat volutpat.</p>
  <a class="abs btn-blue testimonials" href="#">SEE TESTIMONIALS</a>
</section>
<div class="abs rule" style="top:2593px"></div>

<section class="contact">
  <p class="abs contact-kicker">LOOKING FOR MORE INFORMATION?</p>
  <h2 class="abs contact-title">GET IN TOUCH WITH US</h2>
  <div class="abs contact-band"></div>
  <div class="abs portrait" role="img" aria-label="Photo of a smiling businessman in glasses, white shirt and dark tie, holding a tablet"></div>
  <p class="abs call-line">Call us at <b>1-555-014-2291</b> or send us a message</p>
  <div class="abs field f-name">Full Name*</div>
  <div class="abs field f-email">Email*</div>
  <div class="abs field f-msg">Message...</div>
  <a class="abs send" href="#">SEND MESSAGE
    <svg width="18" height="14" viewBox="0 0 18 14" fill="none" stroke="#fff" stroke-width="2"><path d="M1 7h15M11 2l5 5-5 5"/></svg>
  </a>
  <p class="abs wish">How Do You Wish To Be<br>Contacted?</p>
  <div class="abs ico-box ico-phone"><svg width="20" height="20" viewBox="0 0 24 24"><path d="M6.6 10.8c1.4 2.8 3.8 5.1 6.6 6.6l2.2-2.2c.3-.3.7-.4 1-.2 1.1.4 2.3.6 3.6.6.6 0 1 .4 1 1V20c0 .6-.4 1-1 1C10.6 21 3 13.4 3 4c0-.6.4-1 1-1h3.5c.6 0 1 .4 1 1 0 1.3.2 2.5.6 3.6.1.3 0 .7-.2 1z" fill="#0b5cab"/></svg></div>
  <div class="abs ico-box ico-mail"><svg width="22" height="16" viewBox="0 0 22 16"><rect x="1" y="1" width="20" height="14" fill="#0b5cab"/><path d="M1 1l10 8 10-8" fill="none" stroke="#fff" stroke-width="1.5"/></svg></div>
</section>

<footer class="abs footer"></footer>
<a class="abs brand f-brand" href="#"><span class="brand-mark"></span><span class="brand-name" style="font-size:20px">Dulvane</span></a>
<p class="abs copy">©2016</p>
<div class="abs f-sep"></div>
<ul class="abs f-links">
  <li class="active">HOME</li><li>CANDIDATE PORTAL</li><li>CONTACT US</li><li>BLOG</li><li>SITEMAP</li><li>PRIVACY POLICY</li>
</ul>
<div class="abs social f-social"><span aria-label="Social profile 1"></span><span aria-label="Social profile 2"></span></div>
<a class="abs to-top" href="#"><svg width="22" height="12" viewBox="0 0 22 12" fill="none" stroke="#b9c0c8" stroke-width="2"><path d="M2 10l9-8 9 8"/></svg></a>

</body>
</html>
```